Brightstep Podiatry Needs a Branded 8.5 x 11 template

We need a single template that will reflect our brand and have a really interesting and catchy feel. Be creative. It should include our logo a catch phrase like "Where Your Feet Are in Good Hands" and editable. There should be a header with this information. The central portion should be available to place text about medical conditions or other information and available to take pictures.
The footer needs to be all of the info on our location such as address, phone, drs names etc. - see must haves
We like shadows, 3D, really creative and catchy.
Below is an example that my friend uses. I like it but would like something a little more interesting. I do not want the same design as the flyer attached.
Logo is attached.
Our Colors: Want plenty of white space
#FAC000
#9F38AA

Target Market(s)

Patients and Physicians. We are podiatrists, foot and ankle specialists but I do not want any pictures of feet or medical stuff on the template.

Industry/Entity Type

Medical

Requirements
Must have
• For the Footer: Make it creative please

Physicians and Surgeons of the Foot and Ankle
Dr. Owen Pruitt
Dr. Carla Wendham
Address 4726 W. Bellrose Ave. Suite 418, Tampa, FL 33614
phone - 813-642-0917
email office@brightsteppodiatrymail.com
web http://www.theGulfcrestFootDoc.com

The Tagline section in the header needs to be editable so I can make changes. The middle section also needs to be editable.

I prefer to make edits in Photoshop or possibly Illustrator

```html
<!DOCTYPE html>
<html lang="en">
<head>
<meta charset="utf-8">
<title>Brightstep Podiatry Flyer</title>
<link rel="stylesheet" href="https://fonts.googleapis.com/css2?family=Lato:ital,wght@0,400;0,700;1,400;1,700;1,900&family=Cormorant+Garamond:wght@500;600&display=swap">
<style>
  :root {
    --purple: #9F38AA;
    --purple-deep: #7d2a8a;
    --gold: #FAC000;
    --cream: #f6f7e4;
    --ink: #2a2a2a;
    --white: #ffffff;
  }
  * { margin: 0; padding: 0; box-sizing: border-box; }
  html, body { width: 921px; height: 1200px; overflow: hidden; background: #ececec; }
  .flyer {
    position: relative;
    width: 921px;
    height: 1200px;
    overflow: hidden;
    background: linear-gradient(180deg, #eef2d6 0%, var(--cream) 35%, #fbfbf0 100%);
    font-family: "Lato", sans-serif;
  }
  .hero-photo {
    position: absolute;
    left: 330px; top: 0;
    width: 591px; height: 560px;
    background: radial-gradient(ellipse at 60% 45%, #e3b9a6 0%, #f2ddd2 35%, #fbf7f4 70%, #ffffff 100%);
  }
  .brand {
    position: absolute;
    left: 46px; top: 100px;
    display: flex; align-items: center; gap: 12px;
  }
  .brand-dot { width: 22px; height: 22px; border-radius: 50%; background: var(--purple); }
  .brand-name { font-size: 42px; font-weight: 400; color: var(--ink); letter-spacing: 0.2px; }
  .tagline {
    position: absolute;
    left: 34px; top: 196px;
    font-family: "Cormorant Garamond", serif;
    font-weight: 600;
    font-variant: small-caps;
    color: var(--purple);
    font-size: 54px;
    line-height: 61px;
  }
  .swoosh { position: absolute; left: 0; top: 420px; width: 921px; height: 160px; }
  .did-you-know {
    position: absolute;
    left: 30px; top: 512px;
    padding: 4px 18px 6px 16px;
    background: var(--purple);
    border-radius: 0 12px 12px 0;
    color: var(--gold);
    font-weight: 900;
    font-style: italic;
    font-size: 27px;
    text-shadow: 1px 2px 2px rgba(0,0,0,0.55);
  }
  .body-copy {
    position: absolute;
    left: 46px; top: 566px;
    width: 850px;
    font-size: 13.6px;
    line-height: 17.5px;
    color: var(--ink);
  }
  .body-copy p { margin-bottom: 14px; }
  .care-photo {
    position: absolute;
    left: 0; top: 910px;
    width: 300px; height: 290px;
    border-top-right-radius: 300px 240px;
    border-top: 5px solid var(--purple);
    border-right: 5px solid var(--gold);
    background: linear-gradient(135deg, #f1cdb4 0%, #e7b59a 45%, #fbeee4 100%);
  }
  .specialty {
    position: absolute;
    left: 322px; top: 944px;
    color: var(--purple);
    font-weight: 700;
    font-size: 24px;
  }
  .doctors {
    position: absolute;
    right: 26px; top: 984px;
    text-align: right;
    font-style: italic;
    font-size: 19px;
    line-height: 25px;
    color: var(--ink);
  }
  .contact-band {
    position: absolute;
    left: 300px; top: 1042px;
    width: 621px; height: 158px;
    background: linear-gradient(90deg, var(--purple-deep), var(--purple));
    border-top: 3px solid var(--gold);
  }
  .contact-list {
    position: absolute;
    left: 322px; top: 1056px;
    list-style: none;
    color: var(--white);
    font-weight: 700;
    font-size: 19px;
    line-height: 31px;
  }
  .contact-list li { display: flex; align-items: center; gap: 10px; }
  .contact-list svg { width: 18px; height: 18px; flex: none; }
</style>
</head>
<body>
<main class="flyer">
  <div class="hero-photo" role="img" aria-label="Photo of bare feet standing on a reflective water surface"></div>

  <div class="brand">
    <span class="brand-dot"></span>
    <span class="brand-name">Brightstep Podiatry</span>
  </div>

  <h1 class="tagline">Where Your<br>Feet Are in<br>Good Hands</h1>

  <svg class="swoosh" viewBox="0 0 921 160" preserveAspectRatio="none" aria-hidden="true">
    <path d="M0 20 C250 -15 600 20 921 145 L921 150 C600 80 300 80 0 80 Z" fill="#9F38AA"/>
    <path d="M0 80 C300 80 600 82 921 152 L921 158 C600 92 300 86 0 86 Z" fill="#FAC000"/>
  </svg>

  <div class="did-you-know">Did you know</div>

  <section class="body-copy">
    <p>Lorem ipsum dolor sit amet, consectetur adipisicing elit, sed do eiusmod tempor incididunt ut labore et dolore magna aliqua. Ut enim ad minim veniam, quis nostrud exercitation ullamco laboris nisi ut aliquip ex ea commodo consequat. Duis aute irure dolor in reprehenderit in voluptate velit esse cillum dolore eu fugiat nulla pariatur. Excepteur sint occaecat cupidatat non proident, sunt in culpa qui officia deserunt mollit anim id est laborum.</p>
    <p>Lorem ipsum dolor sit amet, consectetur adipisicing elit, sed do eiusmod tempor incididunt ut labore et dolore magna aliqua. Ut enim ad minim veniam, quis nostrud exercitation ullamco laboris nisi ut aliquip ex ea commodo consequat. Duis aute irure dolor in reprehenderit in voluptate velit esse cillum dolore eu fugiat nulla pariatur. Excepteur sint occaecat cupidatat non proident, sunt in culpa qui officia deserunt mollit anim id est laborum.</p>
    <p>Lorem ipsum dolor sit amet, consectetur adipisicing elit, sed do eiusmod tempor incididunt ut labore et dolore magna aliqua. Ut enim ad minim veniam, quis nostrud exercitation ullamco laboris nisi ut aliquip ex ea commodo consequat. Duis aute irure dolor in reprehenderit in voluptate velit esse cillum dolore eu fugiat nulla pariatur. Excepteur sint occaecat cupidatat non proident, sunt in culpa qui officia deserunt mollit anim id est laborum.</p>
    <p>Lorem ipsum dolor sit amet, consectetur adipisicing elit, sed do eiusmod tempor incididunt ut labore et dolore magna aliqua. Ut enim ad minim veniam, quis nostrud exercitation ullamco laboris nisi ut aliquip ex ea commodo consequat. Duis aute irure dolor in reprehenderit in voluptate velit esse cillum dolore eu fugiat nulla pariatur. Excepteur sint occaecat cupidatat non proident, sunt in culpa qui officia deserunt mollit anim id est laborum.</p>
  </section>

  <div class="care-photo" role="img" aria-label="Photo of hands massaging a foot"></div>

  <h2 class="specialty">Physicians and Surgeons of the Foot and Ankle</h2>
  <div class="doctors">
    <div>Dr. Owen Pruitt</div>
    <div>Dr. Carla Wendham</div>
  </div>

  <div class="contact-band"></div>
  <ul class="contact-list">
    <li>
      <svg viewBox="0 0 20 20" aria-hidden="true"><circle cx="10" cy="10" r="10" fill="#3b7fc4"/><path d="M10 4 L16 10 H14 V15 H6 V10 H4 Z" fill="#fff"/></svg>
      4726 W. Bellrose Ave. Suite 418, Tampa, FL 33614
    </li>
    <li>
      <svg viewBox="0 0 20 20" aria-hidden="true"><path d="M5 2 L8 6 L6.5 8 C7.5 10.5 9.5 12.5 12 13.5 L14 12 L18 15 L16 18 C9 18 2 11 2 4 Z" fill="#e0463c"/></svg>
      813-642-0917
    </li>
    <li>
      <svg viewBox="0 0 20 20" aria-hidden="true"><rect x="2" y="5" width="16" height="11" rx="1.5" fill="#4b9be0"/><path d="M2 6 L10 12 L18 6" stroke="#fff" stroke-width="1.5" fill="none"/></svg>
      office@brightsteppodiatrymail.com
    </li>
    <li>
      <svg viewBox="0 0 20 20" aria-hidden="true"><circle cx="10" cy="10" r="8" fill="none" stroke="#FAC000" stroke-width="1.6"/><ellipse cx="10" cy="10" rx="3.5" ry="8" fill="none" stroke="#FAC000" stroke-width="1.4"/><path d="M2 10 H18" stroke="#FAC000" stroke-width="1.4"/></svg>
      www.theGulfcrestFootDoc.com
    </li>
  </ul>
</main>
</body>
</html>
```